Heritage Depot Business Cards

Require a business card design. <br/><br/>Needs to include logo (either round or long version) plus these details:<br/>Maya Corvell<br/>Heritage Depot<br/>maya@brightmarttrade.com.au<br/>02 6418 7395<br/>PO Box Glenfarrow NSW 2791<br/>www.heritagedepot.com.au<br/><br/>I need in an editable format so that I can create for multiple staff members. <br/><br/>

Target Market(s)

We are an online store selling renovation products to home owners are builders. Looking for a classic classy design.

Industry/Entity Type

Home And Garden

Contact Information for Business Card

Maya Corvell
Heritage Depot
maya@brightmarttrade.com.au
02 6418 7395
PO Box Glenfarrow NSW 2791
www.heritagedepot.com.au

Colors

Designer to choose colors to be used in the design.

Requirements
Must have
• Must include Logo.

```html
<!DOCTYPE html>
<html lang="en">
<head>
<meta charset="utf-8">
<title>Heritage Depot Business Cards</title>
<link href="https://fonts.googleapis.com/css2?family=Roboto:wght@400;500;700&display=swap" rel="stylesheet">
<style>
  :root {
    --backdrop: #d9d9d9;
    --card-white: #ffffff;
    --card-black: #222222;
    --ink: #1c1c1c;
    --ink-soft: #3a3a3a;
    --foil: #8f8f8f;
    --rule: #2a2a2a;
  }
  * { box-sizing: border-box; margin: 0; padding: 0; }
  html, body {
    width: 1200px; height: 1124px; overflow: hidden;
    background: var(--backdrop);
    font-family: "Roboto", Arial, sans-serif;
  }
  .sheet {
    width: 1200px; height: 1124px;
    display: flex; flex-direction: column;
    align-items: center; justify-content: center; gap: 56px;
  }
  .card {
    width: 840px; height: 480px;
    box-shadow: 0 6px 18px rgba(0,0,0,0.18);
    position: relative;
  }
  .card-back {
    background: var(--card-black);
    display: flex; align-items: center; justify-content: center;
  }
  .brand {
    display: flex; align-items: center; gap: 18px;
  }
  .brand-dot {
    border-radius: 50%;
    flex: none;
  }
  .card-back .brand-dot {
    width: 64px; height: 64px; border: 2px solid var(--foil);
  }
  .card-back .brand-name {
    font-size: 54px; font-weight: 500; color: var(--foil); letter-spacing: 0.5px;
  }
  .card-front {
    background: var(--card-white);
    display: flex; align-items: center;
  }
  .front-brand {
    width: 430px; display: flex; justify-content: center;
  }
  .card-front .brand-dot {
    width: 48px; height: 48px; border: 2px solid var(--ink);
  }
  .card-front .brand-name {
    font-size: 36px; font-weight: 500; color: var(--ink);
  }
  .divider {
    width: 2px; height: 216px; background: var(--rule);
  }
  .details {
    padding-left: 48px; color: var(--ink);
  }
  .person-name { font-size: 28px; font-weight: 700; }
  .person-company { font-size: 20px; color: var(--ink-soft); margin-top: 2px; }
  .address { font-size: 20px; color: var(--ink-soft); margin-top: 22px; line-height: 1.3; }
  .contacts { list-style: none; margin-top: 22px; }
  .contacts li {
    display: flex; align-items: center; gap: 14px;
    font-size: 20px; color: var(--ink-soft); line-height: 1.7;
  }
  .contacts svg { width: 18px; height: 18px; flex: none; }
</style>
</head>
<body>
<main class="sheet">
  <section class="card card-back" aria-label="Card back">
    <div class="brand">
      <span class="brand-dot"></span>
      <span class="brand-name">Heritage Depot</span>
    </div>
  </section>

  <section class="card card-front" aria-label="Card front">
    <div class="front-brand">
      <div class="brand">
        <span class="brand-dot"></span>
        <span class="brand-name">Heritage Depot</span>
      </div>
    </div>
    <div class="divider"></div>
    <div class="details">
      <h1 class="person-name">Maya Corvell</h1>
      <p class="person-company">Heritage Depot</p>
      <p class="address">PO Box Glenfarrow<br>NSW 2791</p>
      <ul class="contacts">
        <li>
          <svg viewBox="0 0 24 24" aria-hidden="true"><path fill="#1c1c1c" d="M6.6 10.8a15.1 15.1 0 0 0 6.6 6.6l2.2-2.2a1 1 0 0 1 1-.25 11.4 11.4 0 0 0 3.6.57 1 1 0 0 1 1 1V20a1 1 0 0 1-1 1A17 17 0 0 1 3 4a1 1 0 0 1 1-1h3.5a1 1 0 0 1 1 1c0 1.25.2 2.45.57 3.57a1 1 0 0 1-.25 1z"/></svg>
          02 6418 7395
        </li>
        <li>
          <svg viewBox="0 0 24 24" aria-hidden="true"><rect x="3" y="5" width="18" height="14" rx="1.5" fill="none" stroke="#1c1c1c" stroke-width="2"/><path d="M3.5 6l8.5 7 8.5-7" fill="none" stroke="#1c1c1c" stroke-width="2"/></svg>
          maya@brightmarttrade.com.au
        </li>
        <li>
          <svg viewBox="0 0 24 24" aria-hidden="true"><circle cx="12" cy="12" r="9" fill="none" stroke="#1c1c1c" stroke-width="2"/><path d="M3 12h18M12 3c3 3.2 3 14.8 0 18M12 3c-3 3.2-3 14.8 0 18" fill="none" stroke="#1c1c1c" stroke-width="1.6"/></svg>
          www.heritagedepot.com.au
        </li>
      </ul>
    </div>
  </section>
</main>
</body>
</html>
```